New Meal Prep Flyer for New Package Deals

We are looking for a design that displays our new packages that we offer. If you take a look at our website www.brambleforkmeals.com, and click on packages , you'll see the way we display them currently . We would like something similar to that in style . The first package is called "Horizon" and this package will be a 1 week package (7 days ), 2 meals a day, for a price of $195.00. The second package is called "Amber" and this package will be a 3 week package (21 days) 2 meals per day, for a price of $546.00 , the third package is a 6 week+ package (45 days), and it is called "Evergreen" , 2 meals per day , and the price is $1080.00 .
For the Amber Package , can you put next to it "Save $42.00!"
For the Evergreen Package, can you put next to it "Save $180!"
We also want our logo on the flyer (see attached), and we are just looking for a 1 page flyer , 8 1/2 x 11.

```html
<!DOCTYPE html>
<html lang="en">
<head>
<meta charset="utf-8">
<title>Bramblefork Meal Prep Packages Flyer</title>
<link href="https://fonts.googleapis.com/css2?family=Montserrat:wght@800&family=Oswald:wght@700&family=Nunito:wght@700;800&display=swap" rel="stylesheet">
<style>
  :root {
    --backdrop: #c9c9c9;
    --paper: #ffffff;
    --charcoal: #3f3f3f;
    --charcoal-light: #5a5a5a;
    --green: #5d9b34;
    --green-light: #8cbc3a;
    --orange: #e8741c;
    --orange-light: #f0a21c;
    --ink: #111111;
    --gold-soft: #f3ead2;
    --food-soft: #e9e0d2;
  }
  * { box-sizing: border-box; margin: 0; padding: 0; }
  html, body { width: 1200px; height: 980px; overflow: hidden; }
  body { background: var(--backdrop); font-family: "Nunito", sans-serif; }

  .flyer {
    position: absolute; left: 240px; top: 24px;
    width: 720px; height: 932px;
    background: var(--paper); overflow: hidden;
    box-shadow: 0 6px 22px rgba(0,0,0,.22);
  }
  .star-band {
    position: absolute; inset: 0 0 auto 0; height: 420px;
    background: linear-gradient(160deg, var(--gold-soft), #fbf7ec 60%, #fff);
  }
  .food-photo {
    position: absolute; left: 0; right: 0; bottom: 0; height: 400px;
    background: linear-gradient(180deg, rgba(255,255,255,0) 0%, var(--food-soft) 35%, #d9cbb5 100%);
  }
  .header-shape { position: absolute; left: 0; top: 0; width: 720px; height: 620px; }

  .brand { position: absolute; left: 120px; top: 150px; width: 560px; text-align: center; }
  .brand-name {
    font-family: "Montserrat", sans-serif; font-weight: 800;
    font-size: 62px; letter-spacing: 1px; color: var(--paper); line-height: 1;
    display: flex; align-items: center; justify-content: center; gap: 12px;
  }
  .brand-dot { width: 18px; height: 18px; border-radius: 50%; background: var(--green-light); }
  .brand-tagline {
    margin-top: 10px; font-family: "Montserrat", sans-serif; font-weight: 800;
    font-size: 22px; color: var(--green-light); letter-spacing: .5px;
  }

  .package {
    position: absolute; width: 210px; border-radius: 34px;
    box-shadow: 4px 6px 12px rgba(0,0,0,.3); color: var(--ink);
  }
  .package--horizon { left: 30px; top: 320px; height: 380px; background: linear-gradient(200deg, var(--green), var(--green-light)); }
  .package--amber { left: 258px; top: 372px; height: 400px; background: linear-gradient(200deg, var(--orange), var(--orange-light)); }
  .package--evergreen { left: 486px; top: 420px; height: 390px; background: linear-gradient(200deg, var(--charcoal-light), var(--charcoal)); }

  .package-name {
    position: absolute; left: 22px; right: 18px; top: 24px; height: 52px;
    border-radius: 26px; display: flex; align-items: center; justify-content: center;
    font-family: "Oswald", sans-serif; font-size: 28px; color: var(--paper);
    box-shadow: 0 3px 6px rgba(0,0,0,.25);
  }
  .package--horizon .package-name, .package--evergreen .package-name { background: linear-gradient(180deg, var(--orange), #d85f12); }
  .package--amber .package-name { background: linear-gradient(180deg, var(--green-light), var(--green)); }

  .package-price {
    position: absolute; left: -6px; right: 12px; top: 96px; height: 60px;
    background: var(--paper); border-radius: 0 30px 30px 0;
    display: flex; align-items: center; justify-content: center;
    font-family: "Oswald", sans-serif; font-size: 36px;
  }
  .package-features { position: absolute; left: 24px; right: 14px; top: 182px; list-style: none; }
  .package-features li {
    display: flex; gap: 10px; align-items: flex-start; margin-bottom: 20px;
    font-weight: 800; font-size: 20px; line-height: 1.05; color: var(--paper);
  }
  .package--amber .package-features li { color: var(--ink); }
  .tick { flex: 0 0 32px; height: 32px; }
  .package-save {
    position: absolute; left: 20px; right: 14px; bottom: 18px; height: 52px;
    background: var(--paper); border-radius: 26px;
    display: flex; align-items: center; justify-content: center; gap: 6px;
    font-weight: 800; font-size: 17px;
  }
  .package-save strong { font-family: "Oswald", sans-serif; font-size: 30px; }

  .website {
    position: absolute; left: 0; right: 0; bottom: 70px; text-align: center;
    font-weight: 800; font-size: 30px; color: var(--ink);
  }
</style>
</head>
<body>
<main class="flyer">
  <div class="star-band" role="img" aria-label="Scattered soft gold star pattern"></div>
  <div class="food-photo" role="img" aria-label="Faded photograph of healthy meal prep bowls with chicken, grains, asparagus and shrimp"></div>

  <svg class="header-shape" viewBox="0 0 720 620" aria-hidden="true">
    <path d="M40 0 H720 V560 C700 500 660 470 600 470 H150 C110 470 100 440 90 400 Z" fill="none" stroke="var(--green)" stroke-width="10"/>
    <path d="M60 0 H720 V540 C700 480 660 450 600 450 H160 C125 450 115 420 105 380 Z" fill="var(--paper)"/>
    <path d="M75 40 H720 V520 C700 460 660 430 600 430 H170 C140 430 130 400 120 360 Z" fill="var(--charcoal)"/>
    <path d="M75 40 C300 0 500 20 720 60" fill="none" stroke="var(--green)" stroke-width="8"/>
    <path d="M75 56 C300 18 500 38 720 78" fill="none" stroke="var(--paper)" stroke-width="6"/>
  </svg>

  <header class="brand">
    <div class="brand-name"><span class="brand-dot"></span>BRAMBLEFORK</div>
    <div class="brand-tagline">HEALTHY KITCHEN | MEAL PREP</div>
  </header>

  <section class="package package--horizon">
    <div class="package-name">Horizon</div>
    <div class="package-price">$195.00</div>
    <ul class="package-features">
      <li><svg class="tick" viewBox="0 0 32 32"><circle cx="16" cy="16" r="13" fill="none" stroke="currentColor" stroke-width="3"/><path d="M9 16 l5 5 l12 -13" fill="none" stroke="currentColor" stroke-width="4"/></svg>1 week package</li>
      <li><svg class="tick" viewBox="0 0 32 32"><circle cx="16" cy="16" r="13" fill="none" stroke="currentColor" stroke-width="3"/><path d="M9 16 l5 5 l12 -13" fill="none" stroke="currentColor" stroke-width="4"/></svg>2 meals per day</li>
    </ul>
  </section>

  <section class="package package--amber">
    <div class="package-name">Amber</div>
    <div class="package-price">$546.00</div>
    <ul class="package-features">
      <li><svg class="tick" viewBox="0 0 32 32"><circle cx="16" cy="16" r="13" fill="none" stroke="currentColor" stroke-width="3"/><path d="M9 16 l5 5 l12 -13" fill="none" stroke="currentColor" stroke-width="4"/></svg>3 week package</li>
      <li><svg class="tick" viewBox="0 0 32 32"><circle cx="16" cy="16" r="13" fill="none" stroke="currentColor" stroke-width="3"/><path d="M9 16 l5 5 l12 -13" fill="none" stroke="currentColor" stroke-width="4"/></svg>2 meals per day</li>
    </ul>
    <div class="package-save">Save <strong>$42!</strong></div>
  </section>

  <section class="package package--evergreen">
    <div class="package-name">Evergreen</div>
    <div class="package-price">$1080.00</div>
    <ul class="package-features">
      <li><svg class="tick" viewBox="0 0 32 32"><circle cx="16" cy="16" r="13" fill="none" stroke="currentColor" stroke-width="3"/><path d="M9 16 l5 5 l12 -13" fill="none" stroke="currentColor" stroke-width="4"/></svg>6 week+ package</li>
      <li><svg class="tick" viewBox="0 0 32 32"><circle cx="16" cy="16" r="13" fill="none" stroke="currentColor" stroke-width="3"/><path d="M9 16 l5 5 l12 -13" fill="none" stroke="currentColor" stroke-width="4"/></svg>2 meals per day</li>
    </ul>
    <div class="package-save">Save <strong>$180!</strong></div>
  </section>

  <p class="website">www.brambleforkmeals.com</p>
</main>
</body>
</html>
```